UI/UX Re-Do for TallyNest - a free to use project management platform for desktop and mobile.

UI/UX Re-Do for TallyNest
TallyNest is a free to use project management platform for desktop and mobile.
We are looking for help with our UI/UX re-design.
As of now the platform is totally functional.
The problem is around flow and look. We want TN to become something that any one can use to manage and even socialize any project. A project can be something work related like organizing a team around a software build, marketing campaign, shared client file space, etc... In fact, most of our current members are using TN for just such work projects.
We also see a project as planning a wedding, organizing a group trip, a simple to-do list, organizing a kids sports team, and so on...
To become a platform that people will use in their work and personal life we first need to become more intuitive and friendly - while maintaining advanced functionality for more advanced needs.
We need help to beautify, streamline, and simplify - while keeping all the functions.
The quickest way to understand TN, and our current issues is this short video:
https://vidhost.example/Qw8ZmT3pLsK
For sure see this link for the entire most recent description AND images:
https://tallynestapp.example/?p=KumrT4WdZeL
The best way to understand TN is to actually use it:
https://tallynestapp.example
Should you choose to take a run at improving TN here are the details:
Please focus your ideas for mobile, it's where we have the biggest issues.
Feel free to get outside the box.
Avoid swipe oriented designs.
Feel free to focus on ideas over polished outputs.
Use any tool you like, PS, hand drawing, written description if you think that works best.
(FYI - we use mostly use Vellum Slides docs internally)
Point is illustration of ideas over tool choice.
Feel free to:
Create something totally new
And/or riff on what we have now
And/or riff on the new design we are considering (see images below)
|||
If we go the direction of the images/designs below the idea is to give people options on how they see/experience TN.
Just below is what we are calling Base Mode. This is a more basic and simple flow. Probably a default to keep new users feeling comfortable at the start.
<img src="https://picbin.example/8hTzqWL.jpg" style="width: 100%;">
https://picbin.example/8hTzqWL.jpg
|||
We are calling this optional view Peak Mode. It is more advanced and can show all project, goal(renamed 'milestones') at the same time. This is more of a paint job on the current design.
<img src="https://picbin.example/vNmd2Rs.jpg" style="width: 100%;">
https://picbin.example/vNmd2Rs.jpg
|||
If you're submitting please let us know if you can also do the PS files for dev.
Not required, but once we nail down the concepts we want someone to hone in the PS files.
As an optional bonus we will also be giving credit to you/your company in TN.
Let us know if you do or don't want that.
We are excited to see your work!!
Target Market(s)
Anyone who needs to organize any project, big or small. The key is to make a super friendly user experience for new users while retaining advanced functions.
Industry/Entity Type
Management
Number of Pages Required
2 page
Look and feel

```html
<!DOCTYPE html>
<html lang="en">
<head>
<meta charset="utf-8">
<title>TallyNest – My Project</title>
<link href="https://fonts.googleapis.com/css2?family=Poppins:wght@400;500;600&display=swap" rel="stylesheet">
<style>
  :root {
    --bar: #2b303c;
    --page: #f6f7fb;
    --white: #ffffff;
    --accent: #ff6b1f;
    --ink: #2b2f3a;
    --muted: #6f7784;
    --faint: #c3c7cf;
    --status: #4cc53a;
    --badge: #0b0b0b;
  }
  * { box-sizing: border-box; margin: 0; padding: 0; }
  html, body { width: 1200px; height: 683px; overflow: hidden; }
  body { background: var(--page); font-family: "Poppins", sans-serif; color: var(--ink); position: relative; }

  .topbar { position: absolute; left: 0; top: 0; width: 1200px; height: 71px; background: var(--bar); }
  .menu-toggle { position: absolute; left: 36px; top: 28px; }
  .brand { position: absolute; left: 89px; top: 22px; color: var(--white); font-weight: 600; font-size: 18px; display: flex; align-items: center; gap: 3px; }
  .brand-dot { width: 5px; height: 5px; border-radius: 50%; background: var(--accent); margin-top: 8px; }
  .search { position: absolute; left: 672px; top: 25px; display: flex; align-items: center; gap: 10px; color: #8d93a0; font-size: 14px; }
  .divider { position: absolute; left: 940px; top: 24px; width: 1px; height: 25px; background: #4a505d; }
  .avatar { position: absolute; left: 960px; top: 13px; width: 45px; height: 45px; border-radius: 50%; background: radial-gradient(circle at 50% 40%, #d9b9a3, #a77e66 60%, #e8e8e8 61%); }
  .user { position: absolute; left: 1014px; top: 25px; color: var(--white); font-size: 14px; display: flex; align-items: center; gap: 6px; }
  .view-switch { position: absolute; left: 1111px; top: 27px; display: flex; gap: 10px; }
  .top-marker { position: absolute; left: 1111px; top: 0; width: 22px; height: 3px; background: var(--accent); }

  .sidebar { position: absolute; left: 89px; top: 127px; width: 332px; }
  .create-btn { height: 56px; background: var(--accent); color: var(--white); border-radius: 3px; display: flex; align-items: center; justify-content: center; position: relative; font-size: 11.5px; font-weight: 500; letter-spacing: .2px; }
  .create-btn svg { position: absolute; right: 14px; }
  .umbrella { position: absolute; left: 0; width: 332px; display: flex; align-items: center; gap: 8px; font-size: 14px; color: var(--ink); }
  .umbrella .more, .project .more { margin-left: auto; }
  .project { position: absolute; left: 0; width: 332px; height: 73px; background: var(--white); border-radius: 4px; padding: 18px 22px; }
  .project-title { font-size: 16.5px; color: var(--ink); }
  .project-status { font-size: 10px; font-weight: 600; color: var(--status); margin-top: 2px; }
  .project-actions { position: absolute; right: 16px; top: 28px; display: flex; align-items: center; gap: 6px; }

  .welcome-panel { position: absolute; left: 466px; top: 127px; width: 645px; height: 556px; background: var(--white); border-radius: 6px 6px 0 0; padding: 55px 65px; }
  .welcome-title { font-size: 33px; font-weight: 400; line-height: 1.2; }
  .welcome-sub { font-size: 16.5px; color: var(--muted); margin-top: 4px; }
  .welcome-sub strong { color: var(--ink); font-weight: 500; }
  .welcome-copy { margin-top: 20px; font-size: 13px; line-height: 28.5px; color: var(--muted); }
  .welcome-copy p + p { margin-top: 10px; }
  .store-links { margin-top: 36px; display: flex; gap: 17px; }
  .store-badge { width: 163px; height: 48px; background: var(--badge); border-radius: 6px; border: 1px solid #a6a6a6; }
</style>
</head>
<body>
  <header class="topbar">
    <svg class="menu-toggle" width="20" height="16" viewBox="0 0 20 16"><g stroke="#fff" stroke-width="2"><line x1="0" y1="1" x2="14" y2="1"/><line x1="0" y1="8" x2="20" y2="8"/><line x1="0" y1="15" x2="12" y2="15"/></g></svg>
    <div class="brand">TallyNest<span class="brand-dot"></span></div>
    <div class="search">
      <svg width="16" height="16" viewBox="0 0 16 16"><circle cx="6.5" cy="6.5" r="5" fill="none" stroke="#8d93a0" stroke-width="2"/><line x1="10.5" y1="10.5" x2="15" y2="15" stroke="#8d93a0" stroke-width="2"/></svg>
      <span>Search here</span>
    </div>
    <div class="divider"></div>
    <div class="avatar" role="img" aria-label="User profile photo"></div>
    <div class="user">Dana R.
      <svg width="8" height="5" viewBox="0 0 8 5"><path d="M1 1l3 3 3-3" fill="none" stroke="#fff" stroke-width="1.3"/></svg>
    </div>
    <div class="view-switch">
      <svg width="22" height="18" viewBox="0 0 22 18"><rect x="0" y="0" width="8" height="18" fill="#fff"/><rect x="10" y="0" width="12" height="18" fill="#fff"/></svg>
      <svg width="24" height="18" viewBox="0 0 24 18"><rect x="0" y="0" width="6" height="18" fill="#5b6170"/><rect x="9" y="0" width="6" height="18" fill="#5b6170"/><rect x="18" y="0" width="6" height="18" fill="#5b6170"/></svg>
    </div>
    <div class="top-marker"></div>
  </header>

  <aside class="sidebar">
    <div class="create-btn">CREATE NEW UMBRELLA
      <svg width="16" height="16" viewBox="0 0 16 16"><g stroke="#fff" stroke-width="1.5"><line x1="8" y1="0" x2="8" y2="16"/><line x1="0" y1="8" x2="16" y2="8"/></g></svg>
    </div>

    <div class="umbrella" style="top:88px">
      <svg width="20" height="12" viewBox="0 0 20 12"><path d="M0 6C3 1 7 0 10 0s7 1 10 6c-3 5-7 6-10 6S3 11 0 6z" fill="#2b2f3a"/><circle cx="10" cy="6" r="3" fill="#fff"/><circle cx="10" cy="6" r="1.6" fill="#2b2f3a"/></svg>
      An Umbrella here
      <svg class="more" width="4" height="16" viewBox="0 0 4 16"><g fill="#b8bcc4"><circle cx="2" cy="2" r="1.4"/><circle cx="2" cy="8" r="1.4"/><circle cx="2" cy="14" r="1.4"/></g></svg>
    </div>

    <div class="project" style="top:125px">
      <div class="project-title">The Big Redesign</div>
      <div class="project-status">STATUS</div>
      <div class="project-actions">
        <svg width="20" height="12" viewBox="0 0 20 12"><path d="M0 6C3 1 7 0 10 0s7 1 10 6c-3 5-7 6-10 6S3 11 0 6z" fill="#c3c7cf"/><circle cx="10" cy="6" r="3" fill="#fff"/><circle cx="10" cy="6" r="1.6" fill="#c3c7cf"/></svg>
        <svg width="4" height="16" viewBox="0 0 4 16"><g fill="#b8bcc4"><circle cx="2" cy="2" r="1.4"/><circle cx="2" cy="8" r="1.4"/><circle cx="2" cy="14" r="1.4"/></g></svg>
      </div>
    </div>

    <div class="project" style="top:205px">
      <div class="project-title">UIX Design project</div>
      <div class="project-status">STATUS</div>
      <div class="project-actions">
        <svg width="20" height="12" viewBox="0 0 20 12"><path d="M0 6C3 1 7 0 10 0s7 1 10 6c-3 5-7 6-10 6S3 11 0 6z" fill="#c3c7cf"/><circle cx="10" cy="6" r="3" fill="#fff"/><circle cx="10" cy="6" r="1.6" fill="#c3c7cf"/></svg>
        <svg width="4" height="16" viewBox="0 0 4 16"><g fill="#b8bcc4"><circle cx="2" cy="2" r="1.4"/><circle cx="2" cy="8" r="1.4"/><circle cx="2" cy="14" r="1.4"/></g></svg>
      </div>
    </div>

    <div class="umbrella" style="top:310px">
      <svg width="20" height="12" viewBox="0 0 20 12"><path d="M0 6C3 1 7 0 10 0s7 1 10 6c-3 5-7 6-10 6S3 11 0 6z" fill="#c3c7cf"/><circle cx="10" cy="6" r="3" fill="#fff"/><circle cx="10" cy="6" r="1.6" fill="#c3c7cf"/></svg>
      Lorem ipsum umbrella here
      <svg class="more" width="4" height="16" viewBox="0 0 4 16"><g fill="#b8bcc4"><circle cx="2" cy="2" r="1.4"/><circle cx="2" cy="8" r="1.4"/><circle cx="2" cy="14" r="1.4"/></g></svg>
    </div>
    <div class="umbrella" style="top:355px">
      <svg width="20" height="12" viewBox="0 0 20 12"><path d="M0 6C3 1 7 0 10 0s7 1 10 6c-3 5-7 6-10 6S3 11 0 6z" fill="#c3c7cf"/><circle cx="10" cy="6" r="3" fill="#fff"/><circle cx="10" cy="6" r="1.6" fill="#c3c7cf"/></svg>
      Ipsum dolor Umbrella dec emit
      <svg class="more" width="4" height="16" viewBox="0 0 4 16"><g fill="#b8bcc4"><circle cx="2" cy="2" r="1.4"/><circle cx="2" cy="8" r="1.4"/><circle cx="2" cy="14" r="1.4"/></g></svg>
    </div>
    <div class="umbrella" style="top:399px">
      <svg width="20" height="12" viewBox="0 0 20 12"><path d="M0 6C3 1 7 0 10 0s7 1 10 6c-3 5-7 6-10 6S3 11 0 6z" fill="#c3c7cf"/><circle cx="10" cy="6" r="3" fill="#fff"/><circle cx="10" cy="6" r="1.6" fill="#c3c7cf"/></svg>
      An aenean commodo Umbrella
      <svg class="more" width="4" height="16" viewBox="0 0 4 16"><g fill="#b8bcc4"><circle cx="2" cy="2" r="1.4"/><circle cx="2" cy="8" r="1.4"/><circle cx="2" cy="14" r="1.4"/></g></svg>
    </div>
  </aside>

  <main class="welcome-panel">
    <h1 class="welcome-title">Welcome!</h1>
    <p class="welcome-sub">this is your <strong>My Project</strong> area!</p>
    <div class="welcome-copy">
      <p>You are currently active on your My Porjects Umbrella. From here you can manage existing projects and create new projects and umbrellas.</p>
      <p>To create a new project look just below the My Projects umbrella and click the Create Project button.</p>
    </div>
    <div class="store-links">
      <div class="store-badge" role="img" aria-label="Mobile app store badge"></div>
      <div class="store-badge" role="img" aria-label="Mobile app store badge"></div>
    </div>
  </main>
</body>
</html>
```